Stationary Design using supplied logo

24 Hour Completion required after acceptance

Business Cards
Letter Head
With Compliments Slips
Web Page Theme

Please only use a the following colors:

Red
Charcoal
Chrome/Silver
White

Red being the DOMINANT Color

Please email questions you may have.

Continued work available to suitably motivated designer.

```html
<!DOCTYPE html>
<html lang="en">
<head>
<meta charset="utf-8">
<title>lumo cash — Stationery Set</title>
<link rel="stylesheet" href="https://fonts.googleapis.com/css2?family=Quicksand:wght@500;700&family=Arimo:wght@400;700&family=Lora:ital@0;1&display=swap">
<style>
  :root {
    --red: #c62f3e;
    --red-soft: #f1d3d6;
    --charcoal: #2b2b2e;
    --silver: #a9abb0;
    --silver-light: #e4e5e8;
    --white: #ffffff;
    --glow: 0 0 22px rgba(255,255,255,.55);
  }
  * { box-sizing: border-box; margin: 0; padding: 0; }
  html, body { width: 1200px; height: 828px; overflow: hidden; }
  body { position: relative; background: var(--red); font-family: "Arimo", Arial, sans-serif; color: var(--charcoal); }

  .masthead { position: absolute; left: 0; top: 0; width: 1200px; height: 87px; background: var(--white); display: flex; flex-direction: column; align-items: center; justify-content: center; }
  .brand { font-family: "Quicksand", sans-serif; font-weight: 700; color: var(--red); display: inline-flex; align-items: center; gap: .25em; white-space: nowrap; line-height: 1; }
  .brand .dot { width: .42em; height: .42em; border-radius: 50%; background: currentColor; display: inline-block; }
  .brand--hero { font-size: 46px; }
  .tagline { font-family: "Arimo", sans-serif; font-weight: 700; font-size: 11px; letter-spacing: 5px; color: var(--charcoal); margin-top: 4px; text-transform: uppercase; }

  .item { position: absolute; background: var(--white); box-shadow: var(--glow); overflow: hidden; }
  .brand--sm { font-size: 19px; }
  .brand--xs { font-size: 14px; }

  /* web page theme */
  .web { left: 30px; top: 155px; width: 400px; height: 282px; }
  .web__topbar { height: 14px; font-size: 5px; color: var(--silver); padding: 4px 8px; border-bottom: 1px solid var(--silver-light); }
  .web__nav { height: 26px; display: flex; align-items: center; justify-content: space-between; padding: 0 10px; border-bottom: 1px solid var(--silver-light); }
  .web__menu { list-style: none; display: flex; gap: 14px; font-size: 6px; color: var(--charcoal); }
  .web__menu .is-active { color: var(--red); border-bottom: 1px solid var(--red); }
  .web__hero { position: absolute; top: 40px; left: 0; width: 400px; height: 162px; background: linear-gradient(120deg, #d9d6d0, #f3f2ef 55%, #e8e7e4); }
  .web__title { position: absolute; left: 18px; top: 52px; background: rgba(255,255,255,.85); padding: 4px 8px; font-family: "Lora", serif; font-size: 16px; }
  .web__services { position: absolute; right: 105px; top: 134px; font-family: "Lora", serif; font-style: italic; font-size: 9px; line-height: 15px; text-align: right; list-style: none; }
  .web__services li:nth-child(2) { margin-right: 22px; }
  .web__services li:nth-child(3) { margin-right: 44px; }
  .web__services li:nth-child(4) { margin-right: 66px; }
  .web__intro { position: absolute; top: 212px; left: 22px; right: 22px; }
  .web__intro h2 { font-family: "Lora", serif; font-style: italic; font-weight: 400; font-size: 8.6px; color: var(--red); white-space: nowrap; }
  .web__intro p { font-size: 5px; color: var(--silver); margin-top: 6px; line-height: 7px; }

  /* letterheads */
  .letter { top: 120px; width: 292px; height: 410px; }
  .letter--one { left: 466px; }
  .letter--two { left: 818px; width: 290px; }
  .letter .brand { position: absolute; left: 22px; top: 32px; }
  .letter__body { position: absolute; left: 22px; top: 82px; width: 252px; font-size: 11px; line-height: 13px; }
  .letter__body p + p { margin-top: 13px; }
  .letter__disc { position: absolute; border-radius: 50%; background: var(--red-soft); opacity: .8; }
  .letter--one .letter__disc { left: -2px; top: 232px; width: 180px; height: 180px; }
  .letter--two .letter__disc { left: 113px; top: 225px; width: 180px; height: 180px; }
  .letter__foot { position: absolute; font-size: 4.5px; color: var(--charcoal); line-height: 6px; }
  .letter--one .letter__foot { right: 18px; bottom: 12px; }
  .letter--two .letter__foot { left: 15px; bottom: 16px; }

  /* business cards */
  .card { top: 498px; width: 133px; height: 75px; }
  .card--back { left: 78px; }
  .card--front { left: 235px; display: flex; align-items: center; justify-content: center; }
  .card__disc { position: absolute; left: 4px; top: 8px; width: 58px; height: 58px; border-radius: 50%; background: var(--red-soft); }
  .card--back .brand { position: absolute; left: 68px; top: 20px; font-size: 10px; }
  .card__details { position: absolute; left: 72px; top: 36px; font-size: 4px; line-height: 5.5px; }
  .card__details strong { font-size: 4.5px; }

  /* envelopes */
  .envelope { width: 329px; height: 172px; }
  .envelope--back { left: 183px; top: 614px; }
  .envelope__flap { position: absolute; top: 0; left: 0; width: 100%; height: 56px; background: var(--red); border-radius: 0 0 60px 60px / 0 0 22px 22px; display: flex; align-items: center; padding-left: 22px; }
  .envelope__flap .brand { color: var(--white); }
  .envelope--front { left: 676px; top: 605px; width: 328px; }
  .envelope--front .brand { position: absolute; left: 40px; top: 36px; }
  .envelope__address { position: absolute; left: 152px; top: 33px; font-size: 4.5px; line-height: 6.5px; }
  .envelope__address .web-link { color: var(--red); }
  .envelope__window { position: absolute; left: 18px; top: 92px; width: 119px; height: 50px; border-radius: 4px; background: var(--red-soft); }
</style>
</head>
<body>

<header class="masthead">
  <span class="brand brand--hero">lumo cash<span class="dot"></span></span>
  <span class="tagline">Savings with a smile</span>
</header>

<section class="item web" aria-label="Web page theme">
  <div class="web__topbar">Tel 01 234 567 · hello@lumocash.com · Open Mon–Fri 9–5</div>
  <nav class="web__nav">
    <span class="brand brand--xs">lumo cash<span class="dot"></span></span>
    <ul class="web__menu">
      <li class="is-active">Home</li><li>Notre agence</li><li>Services</li><li>Portfolio</li><li>Offres</li><li>Blog</li><li>Contact</li>
    </ul>
  </nav>
  <div class="web__hero" role="img" aria-label="Photo of scattered dominoes on a light background"></div>
  <div class="web__title">Divers Solution</div>
  <ul class="web__services">
    <li>Conception &amp; développement</li>
    <li>Search Engine Optimization</li>
    <li>e-Commerce Solutions</li>
    <li>Gestion de contenu</li>
  </ul>
  <div class="web__intro">
    <h2>Bienvenu a notre Site, Lynx Atelier un agence de communication et de publicité</h2>
    <p>Lynx Atelier vous accompagne dans vos projets de communication, de la création graphique au site web, avec des solutions claires et adaptées à vos besoins.</p>
  </div>
</section>

<section class="item letter letter--one" aria-label="Letterhead with text">
  <div class="letter__disc" aria-hidden="true"></div>
  <span class="brand brand--sm">lumo cash<span class="dot"></span></span>
  <div class="letter__body">
    <p>What do you mean by web page theme ? Do you want to design Home page for your website ? Also please send me your logo or any link related to your business so i can start work on your project asap to deliver you quick and best service.</p>
    <p>What do you mean by web page theme ? Do you want to design Home page for your website ? Also please send me your logo or any link related to your business so i can start work on your project asap to deliver you quick and best service.</p>
    <p>What do you mean by web page theme ? Do you want to design Home page for your website ? Also please send me your logo or any link related to your business so i can start work on your project asap to deliver you quick and best service.</p>
  </div>
  <div class="letter__foot">PO Box 815 Millbrook 5520 · Tel 01 234 567</div>
</section>

<section class="item letter letter--two" aria-label="Blank letterhead">
  <div class="letter__disc" aria-hidden="true"></div>
  <span class="brand brand--sm">lumo cash<span class="dot"></span></span>
  <div class="letter__foot">PO Box 815 Millbrook 5520<br>PO Box 815 Millbrook 5520 · Tel 01 234 567</div>
</section>

<section class="item card card--back" aria-label="Business card back">
  <div class="card__disc" aria-hidden="true"></div>
  <span class="brand">lumo cash<span class="dot"></span></span>
  <div class="card__details"><strong>Nora Vale</strong><br>Managing Director<br>01 234 567<br>nora@lumocash.com</div>
</section>

<section class="item card card--front" aria-label="Business card front">
  <span class="brand brand--xs">lumo cash<span class="dot"></span></span>
</section>

<section class="item envelope envelope--back" aria-label="Envelope back">
  <div class="envelope__flap"><span class="brand brand--sm">lumo cash<span class="dot"></span></span></div>
</section>

<section class="item envelope envelope--front" aria-label="Envelope front">
  <span class="brand brand--sm">lumo cash<span class="dot"></span></span>
  <div class="envelope__address">
    PO Box 815 Millbrook 5520 · PO Box 815<br>
    PO Box 815 Millbrook 5520 · Tel 01 234 567<br><br>
    01 234 567 · 01 234 568<br>
    hello@lumocash.com &nbsp;&nbsp;&nbsp;&nbsp;<span class="web-link">www.lumocash.com</span>
  </div>
  <div class="envelope__window" aria-hidden="true"></div>
</section>

</body>
</html>
```